Harbor Business Cards

I need a business card designed with the following information.

Company Name: Harbor Wealth Management
Name: BriAnne Dockery
Title: Executive Assistant
Cell: (555) 555-0173
Direct Line: (555) 555-0148
Email: brianne@harborwmx.com
Address: 20537 W. Marlowe PKWY Ste. B
Larkfield, ZZ 00000

I have attached the logo.
I would like it in navy blue and silver.
Thanks.

```html
<!DOCTYPE html>
<html lang="en">
<head>
<meta charset="utf-8">
<title>Harbor Wealth Management – Business Cards</title>
<link href="https://fonts.googleapis.com/css2?family=Open+Sans:wght@400;600&display=swap" rel="stylesheet">
<style>
  :root {
    --navy: #1d2f57;
    --navy-light: #2b426f;
    --paper: #f7f7f5;
    --silver: #c9ccd2;
    --stage: #e3e3e3;
    --white: #ffffff;
  }
  * { box-sizing: border-box; margin: 0; padding: 0; }
  html, body { width: 1200px; height: 864px; overflow: hidden; }
  body {
    background: var(--stage);
    font-family: "Open Sans", "Segoe UI", Arial, sans-serif;
    display: flex;
    flex-direction: column;
    align-items: center;
    justify-content: center;
    gap: 44px;
  }
  .card {
    width: 660px;
    height: 377px;
    display: flex;
    box-shadow: 0 6px 18px rgba(0,0,0,0.12);
  }
  .card__brand-side {
    width: 50%;
    background: var(--paper);
    display: flex;
    align-items: center;
    justify-content: center;
  }
  .card__navy-side {
    width: 50%;
    background: var(--navy);
    color: var(--white);
  }
  .brand {
    display: flex;
    align-items: center;
    gap: 12px;
    color: var(--navy);
    font-weight: 400;
    font-size: 19px;
    letter-spacing: 0.06em;
    text-transform: uppercase;
    line-height: 1.35;
  }
  .brand__square {
    width: 18px; height: 18px;
    background: var(--navy);
    flex: none;
  }
  .card--back .card__navy-side {
    display: flex;
    align-items: center;
    justify-content: center;
  }
  .brand--large {
    color: var(--white);
    font-size: 26px;
    text-align: center;
  }
  .card--front .card__navy-side {
    background: linear-gradient(135deg, var(--navy-light) 0%, var(--navy) 55%);
    padding: 44px 30px 0 40px;
  }
  .contact__name { font-size: 22px; font-weight: 600; line-height: 1.2; }
  .contact__title { font-size: 17px; font-weight: 400; margin-bottom: 22px; }
  .contact__list { list-style: none; font-size: 16px; line-height: 1.35; }
  .contact__item { display: flex; align-items: flex-start; gap: 12px; }
  .contact__icon {
    flex: none;
    width: 15px; height: 15px;
    margin-top: 3px;
    background: var(--white);
    border-radius: 3px;
    display: flex; align-items: center; justify-content: center;
  }
  .contact__icon svg { width: 11px; height: 11px; fill: var(--navy); }
</style>
</head>
<body>

  <section class="card card--back">
    <div class="card__brand-side">
      <div class="brand"><span class="brand__square"></span><span>Harbor Wealth<br>Management</span></div>
    </div>
    <div class="card__navy-side">
      <div class="brand brand--large">Harbor Wealth<br>Management</div>
    </div>
  </section>

  <section class="card card--front">
    <div class="card__brand-side">
      <div class="brand"><span class="brand__square"></span><span>Harbor Wealth<br>Management</span></div>
    </div>
    <div class="card__navy-side">
      <p class="contact__name">BriAnne Dockery</p>
      <p class="contact__title">Executive Assistant</p>
      <ul class="contact__list">
        <li class="contact__item">
          <span class="contact__icon"><svg viewBox="0 0 12 12"><rect x="3" y="0.5" width="6" height="11" rx="1.2"/><rect x="4" y="2" width="4" height="7" fill="#fff"/></svg></span>
          <span>(555) 555-0173</span>
        </li>
        <li class="contact__item">
          <span class="contact__icon"><svg viewBox="0 0 12 12"><path d="M2.5 1 L4.5 1 L5.3 3.6 L4 4.6 C4.6 6 6 7.4 7.4 8 L8.4 6.7 L11 7.5 L11 9.5 C11 10.3 10.3 11 9.5 11 C5.4 11 1 6.6 1 2.5 C1 1.7 1.7 1 2.5 1 Z"/></svg></span>
          <span>(555) 555-0148</span>
        </li>
        <li class="contact__item">
          <span class="contact__icon"><svg viewBox="0 0 12 12"><rect x="0.5" y="2.5" width="11" height="7" rx="0.8"/><path d="M1 3 L6 7 L11 3" stroke="#fff" stroke-width="1" fill="none"/></svg></span>
          <span>brianne@harborwmx.com</span>
        </li>
        <li class="contact__item">
          <span class="contact__icon"><svg viewBox="0 0 12 12"><path d="M6 0.5 C3.8 0.5 2.2 2.1 2.2 4.3 C2.2 7 6 11.5 6 11.5 C6 11.5 9.8 7 9.8 4.3 C9.8 2.1 8.2 0.5 6 0.5 Z"/><circle cx="6" cy="4.3" r="1.4" fill="#fff"/></svg></span>
          <span>20537 W. Marlowe PKWY Ste. B<br>Larkfield, ZZ 00000</span>
        </li>
      </ul>
    </div>
  </section>

</body>
</html>
```